Bref créative
Design Business Card & Stationary
Talvix Studio
Professional
Derek Holt
4837 Birchwood Lane Suite #210
Fairview, CA 94812
derek@talvixstudio.example
www.talvixstudio.example
This is our logo

```html
<!DOCTYPE html>
<html lang="en">
<head>
<meta charset="utf-8">
<title>Talvix Studio – Business Card</title>
<link rel="stylesheet" href="https://fonts.googleapis.com/css2?family=Source+Sans+3:wght@400;600;700&display=swap">
<style>
  :root {
    --page-bg: #e9e6e1;
    --card-bg: #ffffff;
    --card-shade: #ececec;
    --ink: #2f2f2f;
    --ink-soft: #5b5b5b;
    --accent: #8cbf2f;
    --divider: #cfcfcf;
  }
  * { box-sizing: border-box; margin: 0; padding: 0; }
  html, body {
    width: 1200px;
    height: 965px;
    overflow: hidden;
    background: var(--page-bg);
    font-family: "Source Sans 3", "Helvetica Neue", Arial, sans-serif;
    color: var(--ink);
  }
  .card {
    position: absolute;
    left: 60px;
    top: 182px;
    width: 1080px;
    height: 600px;
    border-radius: 44px;
    background: linear-gradient(180deg, var(--card-bg) 0%, var(--card-bg) 70%, var(--card-shade) 100%);
    box-shadow: 0 18px 40px rgba(0,0,0,0.18);
  }
  .brand {
    position: absolute;
    left: 62px;
    top: 34px;
    display: flex;
    align-items: center;
    gap: 20px;
  }
  .brand-square {
    width: 62px;
    height: 62px;
    background: var(--ink);
  }
  .brand-text { display: flex; flex-direction: column; }
  .brand-name {
    font-size: 52px;
    font-weight: 700;
    line-height: 1;
    color: var(--ink);
    letter-spacing: -0.5px;
  }
  .brand-tagline {
    font-size: 17px;
    font-weight: 600;
    color: var(--ink-soft);
    letter-spacing: 1px;
    margin-top: 4px;
  }
  .person-name {
    position: absolute;
    left: 733px;
    top: 44px;
    font-size: 36px;
    font-weight: 400;
    color: var(--ink-soft);
  }
  .person-name .surname { color: var(--accent); }
  .divider {
    position: absolute;
    left: 594px;
    top: 150px;
    width: 3px;
    height: 300px;
    background: linear-gradient(180deg, rgba(0,0,0,0) 0%, var(--divider) 30%, var(--divider) 70%, rgba(0,0,0,0) 100%);
  }
  .address {
    position: absolute;
    left: 62px;
    top: 204px;
    font-size: 31px;
    line-height: 46px;
    color: var(--ink);
  }
  .contacts {
    position: absolute;
    left: 62px;
    top: 358px;
    font-size: 27px;
    line-height: 36px;
    color: var(--ink-soft);
  }
  .contact-row { display: flex; }
  .contact-label { width: 102px; color: var(--accent); }
  .website {
    position: absolute;
    left: 703px;
    top: 500px;
    font-size: 28px;
    color: var(--ink);
  }
</style>
</head>
<body>
  <div class="card">
    <div class="brand">
      <div class="brand-square"></div>
      <div class="brand-text">
        <span class="brand-name">Talvix Studio</span>
        <span class="brand-tagline">Online Brand Presence Planning</span>
      </div>
    </div>

    <div class="person-name">Derek <span class="surname">Holt</span></div>

    <div class="divider"></div>

    <div class="address">
      <p>4837 Birchwood Lane Suite #210</p>
      <p>Fairview, CA 94812</p>
    </div>

    <div class="contacts">
      <div class="contact-row"><span class="contact-label">Phone</span><span>:619-555-0142</span></div>
      <div class="contact-row"><span class="contact-label">Fax</span><span>:619-555-0178</span></div>
      <div class="contact-row"><span class="contact-label">Email</span><span>:derek@talvixstudio.example</span></div>
    </div>

    <div class="website">www.talvixstudio.example</div>
  </div>
</body>
</html>
```